Design a modern, classy & professional business card for an online real estate agency, specializing in medium-luxury properties in Thailand and later in Singapore and UK.

Possible design ideas so far: (not essential)

- curved corner(s) to the card, white on front & turquoise on back or visa versa.

- front of card - clear and simple, company name in metallic grey/monochrome, logo graphic & company name on front in spot UV or embossed/debossed effect.

- back of card - large, close-cropped, 'ghost' patterns of the C-shaped curves of logo, or company name repeated on back of card in spot UV.

Target Market(s)

- young to middle-aged professionals mainly (but ideally should design should suit all)

- UK, US,EU,AUS & ASIAN mainly (but ideally should design should suit all countries)

Industry/Entity Type

Real Estate

Requirements
Must have
• THEME:
- Luxurious & Modern
- Clean & striking
- Unique & creative

INFO:
- Logo & company name on front
- Contact details on back:

Tobias Lindqvist
Managing Director

www.velmoraestates.example
www.velmoraestates-uk.example

Tel: 083-274-6190
email: tobias@velmoraestates.example

(contact details can be displayed in any order as suites design.)

Nice to have
• - curved corner(s) to the card, white on front & turquoise on back or visa versa.

Should not have
• - No generic images of properties, palm trees/coconut trees etc.

- No other other bold colors, except for main turquoise, grey, metallic white & black theme.

- No obvious business card templates

```html
<!DOCTYPE html>
<html lang="en">
<head>
<meta charset="utf-8">
<title>Velmora Estates – Business Card</title>
<link rel="stylesheet" href="https://fonts.googleapis.com/css2?family=Cormorant+Garamond:wght@500&family=Cormorant+Upright:wght@500&family=Courier+Prime&display=swap">
<style>
  :root {
    --backdrop: #2b2927;
    --card-white: #ffffff;
    --turquoise: #5bbfbf;
    --turquoise-deep: #4aa9a9;
    --steel-grey: #6f6f72;
    --ink: #2f3434;
    --contact-white: #f2fbfb;
  }
  * { margin: 0; padding: 0; box-sizing: border-box; }
  html, body {
    width: 1200px; height: 758px; overflow: hidden;
    background: var(--backdrop);
  }
  .sheet {
    position: relative; width: 1200px; height: 758px;
    display: flex; align-items: center; justify-content: center; gap: 60px;
  }
  .card {
    position: relative; width: 500px; height: 300px;
    border-radius: 32px; overflow: hidden;
  }
  /* Front */
  .card-front { background: var(--card-white); }
  .brand {
    position: absolute; left: 52px; top: 92px;
    display: flex; align-items: center; gap: 22px;
  }
  .brand-square {
    width: 96px; height: 96px; background: var(--turquoise);
  }
  .brand-name {
    font-family: "Cormorant Garamond", Georgia, serif;
    font-weight: 500; font-size: 52px; line-height: 1;
    color: var(--steel-grey);
  }
  .front-holder {
    position: absolute; right: 40px; top: 206px; text-align: right;
  }
  /* Shared name block */
  .holder-name {
    font-family: "Cormorant Upright", Georgia, serif;
    font-weight: 500; font-size: 28px; line-height: 1;
    color: var(--ink);
  }
  .holder-title {
    font-family: "Cormorant Garamond", Georgia, serif;
    font-size: 12px; letter-spacing: 0.5px;
    color: var(--ink);
  }
  /* Back */
  .card-back { background: var(--turquoise); }
  .back-holder { position: absolute; left: 36px; top: 118px; }
  .contact-list {
    position: absolute; left: 36px; bottom: 34px;
    list-style: none;
    font-family: "Courier Prime", "Courier New", monospace;
    font-size: 14px; line-height: 22px; color: var(--contact-white);
  }
  .contact-list li { display: flex; align-items: center; gap: 8px; }
  .contact-icon { width: 13px; height: 13px; flex: none; }
</style>
</head>
<body>
<main class="sheet">
  <section class="card card-front" aria-label="Card front">
    <div class="brand">
      <div class="brand-square"></div>
      <div class="brand-name">Velmora Estates</div>
    </div>
    <div class="front-holder">
      <div class="holder-name">Tobias Lindqvist</div>
      <div class="holder-title">Managing Director</div>
    </div>
  </section>

  <section class="card card-back" aria-label="Card back">
    <div class="back-holder">
      <div class="holder-name">Tobias Lindqvist</div>
      <div class="holder-title">Managing Director</div>
    </div>
    <ul class="contact-list">
      <li>
        <svg class="contact-icon" viewBox="0 0 16 16" aria-hidden="true"><circle cx="8" cy="8" r="8" fill="#2f3434"/><path d="M2 8h12M8 1.5c-3 3.5-3 9.5 0 13M8 1.5c3 3.5 3 9.5 0 13" stroke="#5bbfbf" stroke-width="1.2" fill="none"/></svg>
        www.velmoraestates.example
      </li>
      <li>
        <svg class="contact-icon" viewBox="0 0 16 16" aria-hidden="true"><circle cx="8" cy="8" r="8" fill="#2f3434"/><path d="M2 8h12M8 1.5c-3 3.5-3 9.5 0 13M8 1.5c3 3.5 3 9.5 0 13" stroke="#5bbfbf" stroke-width="1.2" fill="none"/></svg>
        www.velmoraestates-uk.example
      </li>
      <li>
        <svg class="contact-icon" viewBox="0 0 16 16" aria-hidden="true"><path d="M4 1h3l1 4-2 1.5c1 2 2.5 3.5 4.5 4.5L12 9l4 1v3c0 1.5-1 2.5-2.5 2.5C7 15 1 9 1 3.5 1 2 2 1 4 1z" fill="#2f3434"/></svg>
        Tel: 083-274-6190
      </li>
      <li>
        <svg class="contact-icon" viewBox="0 0 16 16" aria-hidden="true"><rect x="1" y="3" width="14" height="10" fill="#2f3434"/><path d="M1.5 3.5 8 9l6.5-5.5" stroke="#5bbfbf" stroke-width="1.2" fill="none"/></svg>
        email: tobias@velmoraestates.example
      </li>
    </ul>
  </section>
</main>
</body>
</html>
```